Velvet Heron Website

We need a website for our software / project management services company based in South Africa called "Velvet Heron". We provide professional services to high value clients in the public and private sectors.

The website must present a highly professional company that exudes quality and confidence.

The theme should be a highly professional subdued look with a fairly limited palette. The neutral tone should be slightly offset with the colours from the company logo. The website should not look dead though, and subtle colour highligting should provide a fresh vibrant feel.

Refer to the current website for general content (www.velvetheron-example.co.za) that may be used. We would also like to make use of social integration and google maps.
Updates

Thanks to all the designers that have participated so far and to those that are cooking something up at this very minute :-)

We have received a lot of designs with elements that we absolutely love. So now the hard work of refining these designs can begin.

We'll try and provide feedback on every design received so far ... and await the beautiful designs that we haven't received yet :-)

Good Luck!

Reason: After careful consideration we are extending the deadline to make small revisions to some of the designs and to select the top three designs. Thank you for everyone who has made a contribution so far - we have several designs that we like and selecting the best one is proving to be difficult :-)

Target Market(s)

The company deals mostly with other businesses, so mostly B2B.

Industry/Entity Type

Software

Requirements
Nice to have
• Social integration

```html
<!DOCTYPE html>
<html lang="en">
<head>
<meta charset="utf-8">
<title>Velvet Heron</title>
<link rel="stylesheet" href="https://fonts.googleapis.com/css2?family=Open+Sans:wght@300;400;600;700&family=PT+Sans+Narrow:wght@700&family=Varela+Round&display=swap">
<style>
  :root {
    --bg: #e6e6e6;
    --band: #f1f1f1;
    --text: #6e6e6e;
    --heading: #7a7a7a;
    --dark: #555;
    --green: #6aab1e;
    --blue: #2a5699;
    --link: #2b5b94;
    --dash: #c4c4c4;
    --pill-grey: #a9a9a9;
  }
  * { box-sizing: border-box; margin: 0; padding: 0; }
  html, body { width: 1200px; height: 955px; overflow: hidden; background: var(--bg); }
  body { font-family: "Open Sans", Verdana, sans-serif; color: var(--text); }
  .page { position: relative; width: 1200px; height: 955px; overflow: hidden; background: linear-gradient(#dcdcdc, #e8e8e8 110px, #e6e6e6); }
  .abs { position: absolute; }

  .brand { display: flex; align-items: center; gap: 8px; font-weight: 700; color: var(--dark); white-space: nowrap; }
  .brand-dot { width: 20px; height: 20px; border-radius: 50%; background: var(--green); flex: none; }
  .header-brand { left: 82px; top: 50px; font-size: 30px; }

  .social { left: 845px; top: 0; width: 303px; height: 38px; background: linear-gradient(#f7f7f7, #e9e9e9); border: 1px solid #d2d2d2; border-top: 0; border-radius: 0 0 6px 6px; display: flex; align-items: center; padding: 0 8px; gap: 6px; font-size: 11.5px; color: #777; white-space: nowrap; }
  .social-label { flex: none; margin-right: 4px; }
  .social-label b { color: var(--green); font-weight: 600; }
  .social-btn { width: 22px; height: 22px; border-radius: 4px; background: #8aa0bf; flex: none; }

  .nav { top: 56px; left: 560px; display: flex; font-family: "PT Sans Narrow", sans-serif; font-weight: 700; font-size: 20px; color: #6b6b6b; white-space: nowrap; }
  .nav a { color: inherit; text-decoration: none; padding: 2px 10px; margin-right: 26px; border-radius: 7px; }
  .nav a:last-child { margin-right: 0; }
  .nav a.active { background: var(--blue); color: #fff; }

  .dashes { left: 80px; width: 1062px; height: 4px; background: repeating-linear-gradient(90deg, var(--dash) 0 12px, transparent 12px 22px); }

  .hero { left: 0; top: 109px; width: 1200px; height: 292px; background: linear-gradient(90deg, #d9d9d9, #e9e9e9 45%, #dedede); }
  .hero-photo { left: 583px; top: 109px; width: 562px; height: 292px; background: linear-gradient(90deg, #e4e4e4 0%, #eaeaea 30%, #d4d4d4 100%); }
  .hero-title { left: 80px; top: 156px; font-family: "Varela Round", sans-serif; font-size: 44px; font-weight: 400; color: var(--heading); letter-spacing: 0.5px; white-space: nowrap; }
  .hero-bar { left: 0; top: 213px; width: 482px; height: 63px; background: linear-gradient(#8fc743, #5f9d18); border-radius: 0 12px 12px 0; }
  .hero-bar span { position: absolute; left: 80px; top: -2px; font-family: "Varela Round", sans-serif; font-size: 54px; color: #f4f4f4; white-space: nowrap; }
  .hero-copy { left: 80px; top: 292px; width: 390px; font-size: 11.4px; line-height: 14.6px; text-align: justify; color: #5c5c5c; }

  .services { left: 0; top: 401px; width: 1200px; height: 215px; background: var(--band); }
  .service { top: 430px; width: 232px; }
  .service h3 { display: flex; align-items: center; gap: 8px; font-size: 13.6px; font-weight: 700; color: var(--green); margin-bottom: 15px; white-space: nowrap; }
  .service h3::before { content: ""; width: 6px; height: 14px; background: var(--blue); clip-path: polygon(0 0, 100% 50%, 0 100%); }
  .service-img { height: 72px; border-radius: 10px; border: 3px solid #fafafa; box-shadow: 0 1px 3px rgba(0,0,0,.2); }
  .service p { margin-top: 14px; font-size: 11px; line-height: 14.6px; text-align: justify; color: #777; }

  .section-title { font-weight: 300; font-size: 24px; color: #666; letter-spacing: -0.5px; white-space: nowrap; }
  .archive { left: 392px; top: 656px; width: 90px; height: 18px; border-radius: 9px 0 0 9px; background: linear-gradient(#dedede, #c8c8c8); font-size: 11px; color: #555; text-align: right; padding: 1px 6px 0 0; white-space: nowrap; }
  .archive b { font-weight: 700; }

  .date { display: inline-block; border-radius: 9px; font-size: 11px; font-weight: 700; color: #fff; padding: 1px 10px; margin-right: 10px; }
  .date.current { background: var(--blue); }
  .date.past { background: var(--pill-grey); }
  .news-main { left: 80px; top: 706px; width: 402px; }
  .news-main h4, .news-row h4 { font-size: 13.6px; font-weight: 600; color: #555; display: flex; align-items: center; white-space: nowrap; }
  .news-main p { margin-top: 10px; font-size: 11px; line-height: 14.6px; color: #777; }
  .news-row { left: 80px; width: 402px; height: 26px; display: flex; align-items: center; border-bottom: 2px solid #d0d0d0; }
  .news-row.shaded { background: #dadada; border-top: 2px solid #d0d0d0; }

  .why-copy { left: 517px; top: 706px; width: 286px; font-size: 11px; line-height: 14.6px; color: #777; }
  .why-list { left: 540px; top: 800px; list-style: none; font-size: 11px; white-space: nowrap; }
  .why-list li { height: 24px; display: flex; align-items: center; gap: 8px; }
  .why-list li::before { content: ""; width: 6px; height: 7px; background: var(--green); clip-path: polygon(0 0, 100% 50%, 0 100%); }
  .why-list a { color: var(--link); }

  .map { left: 840px; top: 706px; width: 274px; height: 92px; border-radius: 6px; border: 2px solid #f8f8f8; background: linear-gradient(135deg, #ece7d8, #dcd8cc 60%, #e6e2d4); }
  .contact-brand { left: 846px; top: 826px; font-size: 19px; }
  .contact-brand .brand-dot { width: 14px; height: 14px; }
  .address { left: 1002px; top: 808px; font-size: 12px; font-weight: 700; line-height: 15px; color: #666; font-style: normal; white-space: nowrap; }

  .footer-left { left: 80px; top: 920px; font-size: 11.5px; color: #666; white-space: nowrap; }
  .footer-left b { color: var(--green); }
  .footer-right { right: 86px; top: 918px; font-size: 16px; color: #888; white-space: nowrap; }
  .footer-right span { color: var(--link); }
  .footer-right i { font-style: normal; color: #aaa; margin: 0 12px; }
</style>
</head>
<body>
<div class="page">
  <header>
    <div class="abs brand header-brand"><span class="brand-dot"></span>Velvet Heron</div>
    <div class="abs social">
      <span class="social-label">OUR COMPANY INTO <b>SOCIAL MEDIA</b>:</span>
      <span class="social-btn"></span><span class="social-btn"></span><span class="social-btn"></span>
    </div>
    <nav class="abs nav">
      <a class="active" href="#">HOME PAGE</a><a href="#">ABOUT US</a><a href="#">OUR OFFER</a><a href="#">PORTFOLIO</a><a href="#">CONTACT</a>
    </nav>
  </header>

  <section>
    <div class="abs hero"></div>
    <div class="abs dashes" style="top:105px"></div>
    <div class="abs hero-photo" role="img" aria-label="Businessman sketching a strategy diagram on a glass board"></div>
    <h1 class="abs hero-title">Lorem ipsum dolor</h1>
    <div class="abs hero-bar"><span>sit amet enim</span></div>
    <p class="abs hero-copy">Velvet Heron is a premium ICT solutions provider which delivers quality software development support services to clients in all sectors of industry. Our value proposition builds on customers’ needs to successfully implement software development projects within a given set of time, quality and budgetary constraints […]</p>
  </section>

  <section>
    <div class="abs services"></div>
    <div class="abs service" style="left:80px">
      <h3>Software Development</h3>
      <div class="service-img" role="img" aria-label="Close-up of source code on paper" style="background:linear-gradient(120deg,#e9e9e9,#bfbfbf)"></div>
      <p>Lorem ipsum dolor sit amet enim. Etiam ullamcorper. Suspendisse a pellentesque dui, non felis. Maecenas malesuada elit felis.</p>
    </div>
    <div class="abs service" style="left:348px">
      <h3>Project Management</h3>
      <div class="service-img" role="img" aria-label="Hand drawing a team structure chart" style="background:linear-gradient(90deg,#e8d8d4,#eee4ec 50%,#d8c6dc)"></div>
      <p>Lorem ipsum dolor sit amet enim. Etiam ullamcorper. Suspendisse a pellentesque dui, non felis. Maecenas malesuada elit felis.</p>
    </div>
    <div class="abs service" style="left:615px">
      <h3>Professional Consulting</h3>
      <div class="service-img" role="img" aria-label="Business team meeting around a table" style="background:linear-gradient(90deg,#7a6a58,#b3a38c 50%,#d8cbb8)"></div>
      <p>Lorem ipsum dolor sit amet enim. Etiam ullamcorper. Suspendisse a pellentesque dui, non felis. Maecenas malesuada elit felis.</p>
    </div>
    <div class="abs service" style="left:883px">
      <h3>Software Quality Assurance</h3>
      <div class="service-img" role="img" aria-label="Interlocking steel gears in blue light" style="background:linear-gradient(120deg,#3e5f94,#8aa3c8 55%,#4a6ea8)"></div>
      <p>Lorem ipsum dolor sit amet enim. Etiam ullamcorper. Suspendisse a pellentesque dui, non felis. Maecenas malesuada elit felis.</p>
    </div>
    <div class="abs dashes" style="top:614px"></div>
  </section>

  <section>
    <h2 class="abs section-title" style="left:80px;top:649px">Fresh news</h2>
    <div class="abs archive">Go to <b>archive</b></div>
    <article class="abs news-main">
      <h4><span class="date current">8 Jun</span>Phasellus fermentum in, dolor.</h4>
      <p>Integer aliquam purus. Quisque lorem tortor fringilla sed, vestibulum id, eleifend justo vel bibendum sapien massa ac turpis faucibus orci luctus non, consectetuer lobortis quis, varius in, purus. Integer ultrices posuere cubilia Curae, Nulla ipsum dolor lacus, suscipit adipiscing.</p>
    </article>
    <div class="abs news-row shaded" style="top:803px"><h4><span class="date past">5 Jun</span>Aliquam erat ac ipsum.</h4></div>
    <div class="abs news-row" style="top:831px"><h4><span class="date past">5 Jun</span>Aliquam erat ac ipsum.</h4></div>

    <h2 class="abs section-title" style="left:515px;top:649px">Why our company?</h2>
    <p class="abs why-copy">Quisque lorem tortor fringilla sed, vestibulum id, eleifend justo vel bibendum sapien massa ac turpis faucibus orci luctus non, consectetuer lobortis quis, varius in, purus. Integer ultrices posuere cubilia Curae, Nulla ipsum dolor lacus, suscipit adipiscing.</p>
    <ul class="abs why-list">
      <li><a href="#">Cum sociis natoque penatibus et ultrices.</a></li>
      <li><a href="#">Nullam wisi ultricies a, gravida vitae, dapibus.</a></li>
      <li><a href="#">Tempor diam pede cursus vitae, ultricies eu.</a></li>
    </ul>

    <h2 class="abs section-title" style="left:837px;top:649px">Contact details</h2>
    <div class="abs map" role="img" aria-label="Street map showing the office location"></div>
    <div class="abs brand contact-brand"><span class="brand-dot"></span>Velvet Heron</div>
    <address class="abs address">42 Protea Lane<br>Hillcrest Park<br>Pretoria,<br>0000.</address>
  </section>

  <footer>
    <div class="abs dashes" style="top:900px"></div>
    <p class="abs footer-left">All rights reserved by <b>VelvetHeron-example.co.za</b></p>
    <p class="abs footer-right">E-mail: <span>info@velvetheron-example.co.za</span><i>|</i>Tel: <span>+27 12 555 0148</span></p>
  </footer>
</div>
</body>
</html>
```